Modern looking signage for dental office.

Exterior signage for passing cars
Updates
Need extra days to review
Target Market(s)
Cars passing by
Font styles to use
Sans Serif
Colors
3276b5
Requirements
Must have
- Logo
- OPEN ON SUTURDAY AND SUNDAY
- NIGHT CLINIC AVAILABLE
- PLEASE USE THE FONT TYPE IN FILE 4 UPLOADED BELOW.
- (847) 302-4496
- Modern looking

```html
<!DOCTYPE html>
<html lang="en">
<head>
<meta charset="utf-8">
<title>Luma Dental – Exterior Sign</title>
<link href="https://fonts.googleapis.com/css2?family=Arimo:wght@400;700&family=Roboto+Condensed:wght@400&display=swap" rel="stylesheet">
<style>
  :root {
    --brand-blue: #0f5499;
    --accent-blue: #3276b5;
    --band-grey: #858585;
    --ink: #141414;
    --paper: #ffffff;
    --backdrop: #eceef1;
  }
  html, body {
    margin: 0;
    padding: 0;
    width: 1200px;
    height: 1200px;
    overflow: hidden;
    background: var(--backdrop);
  }
  .canvas {
    position: relative;
    width: 1200px;
    height: 1200px;
  }
  .sign {
    position: absolute;
    left: 50px;
    top: 240px;
    width: 1100px;
    height: 720px;
    box-shadow: 0 12px 30px rgba(0,0,0,0.18);
  }
  .brand-name {
    font-family: "Arimo", Arial, sans-serif;
    font-weight: 400;
    letter-spacing: 4px;
  }
  .tagline {
    font-family: "Roboto Condensed", "Arial Narrow", sans-serif;
    letter-spacing: 1px;
  }
  .headline,
  .phone,
  .hours {
    font-family: "Arimo", Arial, sans-serif;
    font-weight: 700;
  }
</style>
</head>
<body>
<div class="canvas">
  <svg class="sign" viewBox="0 0 1100 720" xmlns="http://www.w3.org/2000/svg" aria-label="Luma Dental exterior sign">
    <!-- base panel -->
    <rect class="sign-panel" x="0" y="0" width="1100" height="720" fill="var(--paper)"/>

    <!-- top brand band -->
    <path class="brand-band" d="M0 0 H1100 V330 Q560 345 0 300 Z" fill="var(--brand-blue)"/>
    <path class="upper-swoosh" d="M160 338 Q600 372 1100 345 V380 Q620 400 160 338 Z" fill="var(--brand-blue)"/>

    <!-- brand block -->
    <circle class="brand-circle" cx="190" cy="200" r="78" fill="none" stroke="var(--paper)" stroke-width="3"/>
    <text class="brand-name" x="300" y="248" font-size="104" fill="var(--paper)">LUMA DENTAL</text>
    <text class="tagline" x="430" y="318" font-size="40" fill="var(--paper)">MODERN GENERAL DENTISTRY</text>

    <!-- headline -->
    <text class="headline" x="150" y="490" font-size="90" fill="var(--ink)">Night Clinic Available</text>

    <!-- lower swoosh and info band -->
    <path class="lower-swoosh" d="M0 520 Q380 492 800 560 Q380 512 0 548 Z" fill="var(--brand-blue)"/>
    <path class="info-band" d="M0 562 Q420 528 800 565 Q960 585 1100 630 V720 H0 Z" fill="var(--band-grey)"/>

    <text class="phone" x="45" y="668" font-size="62" fill="var(--paper)">(847) 302-4496</text>

    <g class="chevrons" fill="none" stroke="var(--brand-blue)" stroke-width="7" stroke-linejoin="miter">
      <polyline points="480,626 496,645 480,664"/>
      <polyline points="498,626 514,645 498,664"/>
    </g>
    <text class="hours" x="530" y="658" font-size="34" fill="var(--paper)">Open on Saturday and Sunday</text>
  </svg>
</div>
</body>
</html>
```